Personal Finance Author needs a postcard

Hi there,

I am a Canadian personal finance author and have published a new book called The Wealth Compass.

I teach Millennials how to create a 6-figure portfolio through investing (https://www.dariafelt.com/)

I'm speaking at some conferences so we were going to print some postcards to hand out to attendees with our info and calls-to-action on them.

I am looking for 4x6 (horizontal) postcard (no space needed for shipping label).

Logos, Headshots and Book Cover:
https://files.cloudvaultex.com/folders/8kQpZrT2mWvN4xLbJ7sHdYc3FgA9eUoRi?usp=sharing

Both sides will be full colour. I would like a clean and simple look. Our main sites are www.DariaFelt.com and www.TheWealthCompassBook.com if you want to get a sense of style and design.
I also uploaded a few marketing materials so you can see the existing designs.

Side 1:
Get Instant Access to your Free Resources - main headline

(small bullets underneath)
- The Wealth Compass Checklist
- Financial Worksheets
- Database of Investment Tools

DariaFelt.com/Resources

At the bottom, include "Don't forget to follow Daria Felt on social media:
Linkedin: @dariafelt7
Facebook: @thewealthcompassbook Instagram: @thewealthcompassbook Twitter: @WealthCompassBk"

Side 2:
Headline - Want to work directly with Daria and The Wealth Compass team to help you make your money grow and stay safe?

Work with us to (bullet point list)...
- Hire Daria as a Keynote Speaker
- Teach Financial Literacy Workshops
- Receive Financial Coaching

Want To Learn More About How We Can Help?
DariaFelt.com/Services

Include my contact info:
Daria Felt
Author | Speaker | Investor
daria@thewealthcompassbook.com
416-555-0187

Target Market(s)

Millennials who want to learn how to save and invest their money. I focus on stock market investing, real estate investing and entrepreneurship.

Industry/Entity Type

Financial Service

Font styles to use
Sans Serif

Colors

Designer to choose colors to be used in the design.

Requirements
Must have
• Photo of Daria Felt
• The Wealth Compass logo
• Green, Gold/Yellow to match existing colours
• modern business style postcard

```html
<!DOCTYPE html>
<html lang="en">
<head>
<meta charset="utf-8">
<title>The Wealth Compass – Postcard</title>
<link rel="stylesheet" href="https://fonts.googleapis.com/css2?family=Fjalla+One&family=Fira+Sans+Extra+Condensed:wght@300;400;600&display=swap">
<style>
  :root {
    --green: #1f6b35;
    --green-dark: #175a2b;
    --gold: #f29a00;
    --gold-soft: #e2b23a;
    --ink: #3a3a3a;
    --grey: #6b6b6b;
    --rule: #9a9a9a;
    --paper: #ffffff;
    --page: #efefef;
  }
  * { box-sizing: border-box; margin: 0; padding: 0; }
  html, body { width: 862px; height: 1200px; overflow: hidden; }
  body {
    background: var(--page);
    position: relative;
    font-family: "Fira Sans Extra Condensed", "Arial Narrow", sans-serif;
    color: var(--ink);
  }
  .card {
    position: absolute;
    left: 71px;
    width: 721px;
    background: var(--paper);
    overflow: hidden;
  }
  .card--front { top: 67px; height: 480px; }
  .card--back { top: 625px; height: 479px; }

  /* Front */
  .author-visual {
    position: absolute;
    left: 0; top: 0;
    width: 300px; height: 480px;
    background: linear-gradient(160deg, #cfdccf 0%, #e7eee6 45%, #f6f8f5 75%, #ffffff 100%);
  }
  .book-visual {
    position: absolute;
    left: 0; top: 270px;
    width: 320px; height: 210px;
    background: linear-gradient(135deg, #f3f1ea 0%, #e8e4d6 55%, #2d7a3f 100%);
  }
  .headline {
    position: absolute;
    right: 65px; top: 85px;
    font-family: "Fjalla One", "Impact", sans-serif;
    font-size: 40px;
    line-height: 42px;
    color: var(--gold);
    text-align: right;
    text-transform: uppercase;
  }
  .resource-list {
    position: absolute;
    right: 65px; top: 191px;
    list-style: none;
    text-align: right;
    font-weight: 600;
    font-size: 20px;
    line-height: 25px;
    color: var(--green);
  }
  .resource-list li::before { content: "\2022\00a0"; }
  .resource-link {
    position: absolute;
    right: 65px; top: 290px;
    display: flex; align-items: center; gap: 7px;
    font-weight: 600; font-size: 17px;
    color: var(--green);
  }
  .social-heading {
    position: absolute;
    left: 349px; top: 346px;
    width: 307px;
    padding-bottom: 3px;
    border-bottom: 1px solid var(--rule);
    font-weight: 600; font-size: 15px;
    color: var(--green);
  }
  .social-grid {
    position: absolute;
    left: 349px; top: 376px;
    display: grid;
    grid-template-columns: 167px 150px;
    row-gap: 6px;
    font-weight: 300; font-size: 15px;
    color: var(--grey);
  }
  .social-item { display: flex; align-items: center; gap: 5px; }
  .social-mark { width: 17px; height: 17px; flex: none; }
  .social-mark--a { background: #1b74b1; }
  .social-mark--b { background: #c13584; }
  .social-mark--c { background: #3b5b9a; }
  .social-mark--d { background: #2aa3e6; }

  /* Back */
  .back-band {
    position: absolute;
    left: 0; top: 0;
    width: 721px; height: 147px;
    background: linear-gradient(100deg, #24703a 0%, #2f7c45 50%, #24703a 100%);
    display: flex; align-items: center; justify-content: center;
    padding-top: 14px;
  }
  .back-headline {
    font-family: "Fjalla One", "Impact", sans-serif;
    font-size: 28px;
    line-height: 32px;
    color: #ffffff;
    text-align: center;
  }
  .brand-lockup {
    position: absolute;
    left: 80px; top: 190px;
    width: 220px;
    text-align: center;
    font-family: "Fjalla One", "Impact", sans-serif;
    font-size: 46px;
    line-height: 50px;
    text-transform: uppercase;
    color: var(--green-dark);
  }
  .cash-visual {
    position: absolute;
    left: 82px; top: 360px;
    width: 210px; height: 62px;
    background: linear-gradient(100deg, #d9ddcb 0%, #c4cbb1 50%, #e3e5d8 100%);
  }
  .services { position: absolute; left: 349px; top: 196px; width: 330px; }
  .services-title { font-weight: 600; font-size: 17px; color: var(--green); }
  .services-list {
    list-style: none;
    margin: 2px 0 0 14px;
    font-weight: 300; font-size: 16px; line-height: 20px;
  }
  .services-list li::before { content: "\2022\00a0"; color: var(--green); }
  .services-more {
    margin-top: 12px;
    font-weight: 300; font-size: 16px; line-height: 20px;
  }
  .contact { position: absolute; left: 349px; top: 347px; }
  .contact-name { font-weight: 600; font-size: 21px; color: var(--green); }
  .contact-role { font-weight: 300; font-size: 16px; margin-left: 6px; }
  .contact-lines {
    list-style: none;
    margin: 2px 0 0 80px;
    font-weight: 300; font-size: 16px; line-height: 23px;
  }
  .contact-lines li { display: flex; align-items: center; gap: 9px; }
</style>
</head>
<body>

<section class="card card--front">
  <div class="author-visual" role="img" aria-label="Portrait photo of Daria Felt over a pale green banknote background"></div>
  <div class="book-visual" role="img" aria-label="Stack of The Wealth Compass books"></div>

  <h1 class="headline">Get instant access to<br>your free resources</h1>

  <ul class="resource-list">
    <li>The Wealth Compass Checklist</li>
    <li>Financial Worksheets</li>
    <li>Database of Investment Tools</li>
  </ul>

  <p class="resource-link">
    <svg width="16" height="16" viewBox="0 0 16 16" fill="none" stroke="#1f6b35" stroke-width="1.2" aria-hidden="true">
      <circle cx="8" cy="8" r="7"/><ellipse cx="8" cy="8" rx="3" ry="7"/><line x1="1" y1="8" x2="15" y2="8"/>
    </svg>
    dariafelt.com/resources
  </p>

  <p class="social-heading">Don't forget to follow Daria Felt on social media</p>
  <div class="social-grid">
    <span class="social-item"><span class="social-mark social-mark--a"></span>@dariafelt7</span>
    <span class="social-item"><span class="social-mark social-mark--b"></span>@thewealthcompassbook</span>
    <span class="social-item"><span class="social-mark social-mark--c"></span>@thewealthcompassbook</span>
    <span class="social-item"><span class="social-mark social-mark--d"></span>@WealthCompassBk</span>
  </div>
</section>

<section class="card card--back">
  <div class="back-band">
    <h2 class="back-headline">Want to work directly with Daria and The Wealth Compass team<br>to help you make your money grow and stay safe?</h2>
  </div>

  <p class="brand-lockup">The Wealth Compass</p>
  <div class="cash-visual" role="img" aria-label="Fanned stack of banknotes"></div>

  <div class="services">
    <p class="services-title">Work with us to (bullet point list)...</p>
    <ul class="services-list">
      <li>Hire Daria as a Keynote Speaker</li>
      <li>Teach Financial Literacy Workshops</li>
      <li>Receive Financial Coaching</li>
    </ul>
    <p class="services-more">Want To Learn More About How We Can Help?<br>DariaFelt.com/Services</p>
  </div>

  <div class="contact">
    <p><span class="contact-name">Daria Felt</span><span class="contact-role">Author | Speaker | Investor</span></p>
    <ul class="contact-lines">
      <li>
        <svg width="16" height="16" viewBox="0 0 16 16" fill="none" stroke="#1f6b35" stroke-width="1.2" aria-hidden="true">
          <path d="M4 2 L6 5 L5 6.5 C6 8.5 7.5 10 9.5 11 L11 10 L14 12 L12.5 14.5 C7 14 2 9 1.5 3.5 Z"/>
        </svg>
        416-555-0187
      </li>
      <li>
        <svg width="16" height="12" viewBox="0 0 16 12" fill="none" stroke="#1f6b35" stroke-width="1.2" aria-hidden="true">
          <rect x="0.6" y="0.6" width="14.8" height="10.8"/><path d="M0.6 0.6 L8 7 L15.4 0.6"/>
        </svg>
        daria@thewealthcompassbook.com
      </li>
    </ul>
  </div>
</section>

</body>
</html>
```